Bottle design for a range of water enhancers

We need a bottle designed for a new range of water enhancers manufactured by the company, Vello Kettleworks based in Lahore, Pakistan. The product is called "Vello" and comes in 6 different flavors/colors. In essence, Vello is a zero sugar, zero calorie flavor concentrate that is squirted in a glass of water directly from the bottle to make a refreshing beverage. The bottle size is about 60 ml. The bottle needs to be stylish, unique and must have a premium/high-end look to it. The shape of the bottle must be relatively flat. The bottle must be able to translate in to different colors according to the flavor.Some potential sketches have been added for reference.

Target Market(s)

Target market has been identified between the ages of 18 to 35

Colors

Designer to choose colors to be used in the design.

Requirements
Must have
• a sleek, eye catching design.
Nice to have
• A transparent section of the bottle where you can see the liquid inside.
Should not have
• bulky shapes

```html
<!DOCTYPE html>
<html lang="en">
<head>
<meta charset="utf-8">
<title>Vello Liquid Water Enhancer – Flavour Range</title>
<link rel="stylesheet" href="https://fonts.googleapis.com/css2?family=Montserrat:wght@400;700&family=Oswald:wght@300;600&family=Yellowtail&family=Allura&display=swap">
<style>
  :root {
    --page: #ffffff;
    --bottle: #121212;
    --bottle-edge: #2a2a2a;
    --ink: #ffffff;
    --enhancer: #e8262b;
    --red-berry: #d8283f;
    --orange: #e27a25;
    --lemon: #d6d62a;
    --grape: #c23bd6;
    --blue: #2fa6de;
    --kiwi: #b5d334;
  }
  * { box-sizing: border-box; margin: 0; padding: 0; }
  html, body { width: 1200px; height: 900px; overflow: hidden; background: var(--page); }
  .range {
    position: relative;
    width: 1200px; height: 900px;
  }
  .bottle {
    position: absolute;
    width: 218px; height: 403px;
    color: var(--ink);
    text-align: center;
  }
  .bottle--r1 { top: 38px; }
  .bottle--r2 { top: 461px; }
  .bottle--c1 { left: 245px; }
  .bottle--c2 { left: 493px; }
  .bottle--c3 { left: 741px; }
  .bottle--kiwi { top: 454px; }

  .bottle__shape { position: absolute; inset: 0; width: 100%; height: 100%; }
  .bottle__body { fill: var(--bottle); }
  .bottle__cap { fill: #1c1c1c; stroke: #333; stroke-width: 2; }
  .bottle__window { fill: var(--tone); }

  .claim {
    position: absolute; top: 28px; left: 0; width: 100%;
    display: flex; justify-content: center; align-items: flex-start; gap: 2px;
  }
  .claim__pct { font-family: "Montserrat", sans-serif; font-weight: 400; font-size: 29px; line-height: 1; letter-spacing: -1px; }
  .claim__words { position: relative; text-align: left; }
  .claim__natural { font-family: "Allura", cursive; font-size: 27px; line-height: 0.9; display: block; }
  .claim__ingredients { font-family: "Montserrat", sans-serif; font-size: 7px; letter-spacing: 2px; display: block; margin-top: -2px; }

  .brand {
    position: absolute; top: 60px; left: 0; width: 100%;
    font-family: "Montserrat", sans-serif; font-weight: 700;
    font-size: 48px; line-height: 1; letter-spacing: -1px;
  }
  .spaced {
    position: absolute; left: 0; width: 100%;
    font-family: "Montserrat", sans-serif; font-weight: 700;
    font-size: 10px; letter-spacing: 4.5px;
  }
  .spaced--liquid { top: 117px; }
  .spaced--sugar { top: 172px; }
  .enhancer {
    position: absolute; top: 126px; left: 0; width: 100%;
    font-family: "Oswald", sans-serif; font-weight: 600;
    font-size: 35px; line-height: 1.2; color: var(--enhancer);
    -webkit-text-stroke: 1px #fff;
  }
  .fruit {
    position: absolute; top: 198px; left: 58px; width: 102px; height: 82px;
    border-radius: 45%;
    background: radial-gradient(circle at 45% 45%, var(--tone), color-mix(in srgb, var(--tone) 45%, #000) 75%, transparent 76%);
  }
  .flavor {
    position: absolute; top: 298px; left: 0; width: 100%;
    font-family: "Yellowtail", cursive; font-size: 29px; line-height: 1.2;
    color: var(--tone);
  }
  .volume {
    position: absolute; top: 352px; left: 0; width: 100%;
    font-family: "Oswald", sans-serif; font-weight: 300; font-size: 15px; letter-spacing: 1px;
  }
  .servings {
    position: absolute; top: 375px; left: 0; width: 100%;
    font-family: "Oswald", sans-serif; font-weight: 300; font-size: 7.5px; letter-spacing: 1px;
  }
  .bottle__gloss { fill: url(#gloss); pointer-events: none; }
</style>
</head>
<body>
<svg width="0" height="0" style="position:absolute" aria-hidden="true">
  <defs>
    <clipPath id="bottle-clip">
      <path d="M40,0 H360 Q398,0 400,60 C402,200 380,300 372,400 C364,500 392,600 396,690 Q398,740 350,740 H50 Q2,740 4,690 C8,600 36,500 28,400 C20,300 -2,200 0,60 Q2,0 40,0Z"/>
    </clipPath>
    <linearGradient id="shade" x1="0" y1="0" x2="0" y2="1">
      <stop offset="0" stop-color="#000" stop-opacity="0.35"/>
      <stop offset="0.5" stop-color="#fff" stop-opacity="0.12"/>
      <stop offset="1" stop-color="#000" stop-opacity="0.35"/>
    </linearGradient>
    <linearGradient id="gloss" x1="0" y1="0" x2="1" y2="0">
      <stop offset="0" stop-color="#fff" stop-opacity="0"/>
      <stop offset="0.45" stop-color="#fff" stop-opacity="0.55"/>
      <stop offset="0.55" stop-color="#fff" stop-opacity="0.55"/>
      <stop offset="1" stop-color="#fff" stop-opacity="0"/>
    </linearGradient>
    <linearGradient id="side-sheen" x1="0" y1="0" x2="1" y2="0">
      <stop offset="0" stop-color="#fff" stop-opacity="0.12"/>
      <stop offset="0.2" stop-color="#fff" stop-opacity="0"/>
      <stop offset="0.8" stop-color="#fff" stop-opacity="0"/>
      <stop offset="1" stop-color="#fff" stop-opacity="0.12"/>
    </linearGradient>
  </defs>
</svg>

<main class="range">
  <!-- reusable bottle markup per flavour -->
  <section class="bottle bottle--r1 bottle--c1" style="--tone: var(--red-berry)">
    <svg class="bottle__shape" viewBox="0 0 400 740" preserveAspectRatio="none" aria-hidden="true">
      <g clip-path="url(#bottle-clip)">
        <rect class="bottle__body" width="400" height="740"/>
        <path class="bottle__window" d="M0,235 L100,430 L0,600Z"/>
        <path class="bottle__window" d="M400,235 L300,430 L400,600Z"/>
        <path d="M0,235 L100,430 L0,600Z M400,235 L300,430 L400,600Z" fill="url(#shade)"/>
        <rect width="400" height="740" fill="url(#side-sheen)"/>
        <path class="bottle__cap" d="M150,0 Q160,40 200,40 Q240,40 250,0Z"/>
        <rect class="bottle__gloss" x="200" y="0" width="24" height="740"/>
      </g>
    </svg>
    <div class="claim"><span class="claim__pct">100%</span><span class="claim__words"><span class="claim__natural">Natural</span><span class="claim__ingredients">INGREDIENTS</span></span></div>
    <div class="brand">Vello</div>
    <div class="spaced spaced--liquid">LIQUID WATER</div>
    <div class="enhancer">ENHANCER</div>
    <div class="spaced spaced--sugar">SUGAR FREE</div>
    <div class="fruit" role="img" aria-label="Photo of red currants with leaves"></div>
    <div class="flavor">Red Berry</div>
    <div class="volume">60 ML</div>
    <div class="servings">30 SERVINGS 6 LZ OZ PER SERVING</div>
  </section>

  <section class="bottle bottle--r1 bottle--c2" style="--tone: var(--orange)">
    <svg class="bottle__shape" viewBox="0 0 400 740" preserveAspectRatio="none" aria-hidden="true">
      <g clip-path="url(#bottle-clip)">
        <rect class="bottle__body" width="400" height="740"/>
        <path class="bottle__window" d="M0,235 L100,430 L0,600Z"/>
        <path class="bottle__window" d="M400,235 L300,430 L400,600Z"/>
        <path d="M0,235 L100,430 L0,600Z M400,235 L300,430 L400,600Z" fill="url(#shade)"/>
        <rect width="400" height="740" fill="url(#side-sheen)"/>
        <path class="bottle__cap" d="M150,0 Q160,40 200,40 Q240,40 250,0Z"/>
        <rect class="bottle__gloss" x="200" y="0" width="24" height="740"/>
      </g>
    </svg>
    <div class="claim"><span class="claim__pct">100%</span><span class="claim__words"><span class="claim__natural">Natural</span><span class="claim__ingredients">INGREDIENTS</span></span></div>
    <div class="brand">Vello</div>
    <div class="spaced spaced--liquid">LIQUID WATER</div>
    <div class="enhancer">ENHANCER</div>
    <div class="spaced spaced--sugar">SUGAR FREE</div>
    <div class="fruit" role="img" aria-label="Photo of a whole and halved orange"></div>
    <div class="flavor">Pulpy Orange</div>
    <div class="volume">60 ML</div>
    <div class="servings">30 SERVINGS 6 LZ OZ PER SERVING</div>
  </section>

  <section class="bottle bottle--r1 bottle--c3" style="--tone: var(--lemon)">
    <svg class="bottle__shape" viewBox="0 0 400 740" preserveAspectRatio="none" aria-hidden="true">
      <g clip-path="url(#bottle-clip)">
        <rect class="bottle__body" width="400" height="740"/>
        <path class="bottle__window" d="M0,235 L100,430 L0,600Z"/>
        <path class="bottle__window" d="M400,235 L300,430 L400,600Z"/>
        <path d="M0,235 L100,430 L0,600Z M400,235 L300,430 L400,600Z" fill="url(#shade)"/>
        <rect width="400" height="740" fill="url(#side-sheen)"/>
        <path class="bottle__cap" d="M150,0 Q160,40 200,40 Q240,40 250,0Z"/>
        <rect class="bottle__gloss" x="200" y="0" width="24" height="740"/>
      </g>
    </svg>
    <div class="claim"><span class="claim__pct">100%</span><span class="claim__words"><span class="claim__natural">Natural</span><span class="claim__ingredients">INGREDIENTS</span></span></div>
    <div class="brand">Vello</div>
    <div class="spaced spaced--liquid">LIQUID WATER</div>
    <div class="enhancer">ENHANCER</div>
    <div class="spaced spaced--sugar">SUGAR FREE</div>
    <div class="fruit" role="img" aria-label="Photo of lemons with a cut half and juice drops"></div>
    <div class="flavor">Juicy Lemon</div>
    <div class="volume">60 ML</div>
    <div class="servings">30 SERVINGS 6 LZ OZ PER SERVING</div>
  </section>

  <section class="bottle bottle--r2 bottle--c1" style="--tone: var(--grape)">
    <svg class="bottle__shape" viewBox="0 0 400 740" preserveAspectRatio="none" aria-hidden="true">
      <g clip-path="url(#bottle-clip)">
        <rect class="bottle__body" width="400" height="740"/>
        <path class="bottle__window" d="M0,235 L100,430 L0,600Z"/>
        <path class="bottle__window" d="M400,235 L300,430 L400,600Z"/>
        <path d="M0,235 L100,430 L0,600Z M400,235 L300,430 L400,600Z" fill="url(#shade)"/>
        <rect width="400" height="740" fill="url(#side-sheen)"/>
        <path class="bottle__cap" d="M150,0 Q160,40 200,40 Q240,40 250,0Z"/>
        <rect class="bottle__gloss" x="200" y="0" width="24" height="740"/>
      </g>
    </svg>
    <div class="claim"><span class="claim__pct">100%</span><span class="claim__words"><span class="claim__natural">Natural</span><span class="claim__ingredients">INGREDIENTS</span></span></div>
    <div class="brand">Vello</div>
    <div class="spaced spaced--liquid">LIQUID WATER</div>
    <div class="enhancer">ENHANCER</div>
    <div class="spaced spaced--sugar">SUGAR FREE</div>
    <div class="fruit" role="img" aria-label="Photo of a bunch of dark grapes with a leaf" style="--tone:#3a2a3e"></div>
    <div class="flavor">Juicy Grapes</div>
    <div class="volume">60 ML</div>
    <div class="servings">30 SERVINGS 6 LZ OZ PER SERVING</div>
  </section>

  <section class="bottle bottle--r2 bottle--c2" style="--tone: var(--blue)">
    <svg class="bottle__shape" viewBox="0 0 400 740" preserveAspectRatio="none" aria-hidden="true">
      <g clip-path="url(#bottle-clip)">
        <rect class="bottle__body" width="400" height="740"/>
        <path class="bottle__window" d="M0,235 L100,430 L0,600Z"/>
        <path class="bottle__window" d="M400,235 L300,430 L400,600Z"/>
        <path d="M0,235 L100,430 L0,600Z M400,235 L300,430 L400,600Z" fill="url(#shade)"/>
        <rect width="400" height="740" fill="url(#side-sheen)"/>
        <path class="bottle__cap" d="M150,0 Q160,40 200,40 Q240,40 250,0Z"/>
        <rect class="bottle__gloss" x="200" y="0" width="24" height="740"/>
      </g>
    </svg>
    <div class="claim"><span class="claim__pct">100%</span><span class="claim__words"><span class="claim__natural">Natural</span><span class="claim__ingredients">INGREDIENTS</span></span></div>
    <div class="brand">Vello</div>
    <div class="spaced spaced--liquid">LIQUID WATER</div>
    <div class="enhancer">ENHANCER</div>
    <div class="spaced spaced--sugar">SUGAR FREE</div>
    <div class="fruit" role="img" aria-label="Photo of blue raspberries with leaves" style="--tone:#2a3fd8"></div>
    <div class="flavor">Blue Raspberry</div>
    <div class="volume">60 ML</div>
    <div class="servings">30 SERVINGS 6 LZ OZ PER SERVING</div>
  </section>

  <section class="bottle bottle--r2 bottle--c3 bottle--kiwi" style="--tone: var(--kiwi)">
    <svg class="bottle__shape" viewBox="0 0 400 740" preserveAspectRatio="none" aria-hidden="true">
      <g clip-path="url(#bottle-clip)">
        <rect class="bottle__body" width="400" height="740"/>
        <path class="bottle__window" d="M0,235 L100,430 L0,600Z"/>
        <path class="bottle__window" d="M400,235 L300,430 L400,600Z"/>
        <path d="M0,235 L100,430 L0,600Z M400,235 L300,430 L400,600Z" fill="url(#shade)"/>
        <rect width="400" height="740" fill="url(#side-sheen)"/>
        <path class="bottle__cap" d="M150,0 Q160,40 200,40 Q240,40 250,0Z"/>
        <rect class="bottle__gloss" x="200" y="0" width="24" height="740"/>
      </g>
    </svg>
    <div class="claim"><span class="claim__pct">100%</span><span class="claim__words"><span class="claim__natural">Natural</span><span class="claim__ingredients">INGREDIENTS</span></span></div>
    <div class="brand">Vello</div>
    <div class="spaced spaced--liquid">LIQUID WATER</div>
    <div class="enhancer">ENHANCER</div>
    <div class="spaced spaced--sugar">SUGAR FREE</div>
    <div class="fruit" role="img" aria-label="Photo of a whole kiwi and kiwi halves with leaves" style="--tone:#7a9a2a"></div>
    <div class="flavor">Pulpy Kiwi</div>
    <div class="volume">60 ML</div>
    <div class="servings">30 SERVINGS 6 LZ OZ PER SERVING</div>
  </section>
</main>
</body>
</html>
```